Stationery Design Project for Marketing Consultancy

I have started a new consultancy business and require the following elements to be designed using existing logo:
• Business card
• Letterhead
• Envelope (DL, C4, C5)
• Microsoft word template for report writing
• A4 Presentation Folder
• Powerpoint template
COPY FOR FRONT AND BACK OF BUSINESS CARD
logo
'Countable Growth. Bold Outcomes' slogan (but no need to use existing lockup with logo)
name, B Bus. Mktg, Grad Dip Digital Mktg, CPM (post nominal abbreviations in smaller font)
mobile: 04XX-XXX-XXX (I will give details to the winner to add)
website: www.quorvale.com.au
email: info@quorvale.com.au
COPY FOR LETTERHEAD
Logo
Company Name
Please, submit your designs that include business card, letterhead and envelope. Once selected the winner will be asked to complete the project by creating the rest of the artwork.
FINAL FILES
Print ready files to be supplied as well as Indesign files so that minor amends can be made if necessary in future.
• Layered vectors in EPS & PDF
• Screen quality JPEG & PNGs
ABOUT THE BUSINESS: QUORVALE
I work with clients to understand their business challenges, developing and executing Countable Growth strategies tied to key business metrics. Services include:
Services include:
• Business planning and business development
• Marketing and brand strategy
• Insight-driven integrated campaigns
• Loyalty programs and retention marketing
• Marketing automation
• Direct marketing (traditional and digital)
• Content strategy and development
Hi everyone,
Target Market(s)
Corporate decision makers (heads of marketing, general managers etc) and small to medium sized business owners. Predominately male aged 35+
Industry/Entity Type
Marketing
Requirements
Must have
- BRAND PERSONALITY
The successful design will communicate brand personality. I am a professional, results-driven entrepreneur, but want to show off my creative flair.
MEMORABILITY
Looking for a unique and eye-catching design. Am considering special printing effects (die cuts, letterpress, interactive elements, embossing, foiling etc) or a striking minimalist approach.
Nice to have
- I have a mission that could be incorporated on reverse if room -
Turning insights into actions & passion into profit.
Should not have
- Use of pink or green.

```html
<!DOCTYPE html>
<html lang="en">
<head>
<meta charset="utf-8">
<title>Quorvale – A4 Presentation Folder</title>
<link rel="stylesheet" href="https://fonts.googleapis.com/css2?family=Open+Sans:wght@400;600&display=swap">
<style>
  :root {
    --backdrop: #9a9a9a;
    --cover-dark: #464646;
    --cover-mid: #575757;
    --cover-sheen: #6a6a6a;
    --ink-light: #f2f2f2;
    --ink-soft: #d9d9d9;
    --band: #ffffff;
    --band-ink: #333333;
    --emblem: #3a3a3a;
  }
  * { margin: 0; padding: 0; box-sizing: border-box; }
  html, body {
    width: 1200px;
    height: 902px;
    overflow: hidden;
    background: var(--backdrop);
    font-family: "Open Sans", Arial, sans-serif;
  }
  .folder-spread {
    position: relative;
    width: 1200px;
    height: 902px;
  }
  .cover {
    position: absolute;
    top: 112px;
    width: 462px;
    height: 684px;
    overflow: hidden;
    box-shadow: 0 8px 24px rgba(0,0,0,0.28);
  }
  .cover--front { left: 118px; }
  .cover--back { left: 636px; }
  .cover__texture {
    position: absolute;
    inset: 0;
    background:
      linear-gradient(120deg,
        rgba(255,255,255,0) 20%,
        rgba(255,255,255,0.07) 38%,
        rgba(255,255,255,0) 55%),
      linear-gradient(160deg, var(--cover-sheen) 0%, var(--cover-mid) 40%, var(--cover-dark) 100%);
  }
  /* Front cover wordmark */
  .brand-lockup {
    position: absolute;
    right: 76px;
    bottom: 50px;
    text-align: right;
    color: var(--ink-light);
  }
  .brand-lockup__mark {
    display: inline-block;
    width: 76px;
    height: 76px;
    border-radius: 50%;
    background: var(--ink-light);
    margin-bottom: 14px;
  }
  .brand-lockup__name {
    font-size: 42px;
    font-weight: 600;
    letter-spacing: 1px;
    line-height: 1;
  }
  .brand-lockup__tagline {
    font-size: 17px;
    font-weight: 400;
    letter-spacing: 0.3px;
    margin-top: 6px;
    color: var(--ink-soft);
  }
  /* Back cover */
  .mission {
    position: absolute;
    top: 212px;
    left: 0;
    right: 0;
    text-align: center;
    color: var(--ink-light);
  }
  .mission__emblem {
    display: inline-block;
    width: 136px;
    height: 136px;
    border-radius: 50%;
    background: var(--emblem);
    margin-bottom: 26px;
  }
  .mission__line {
    font-size: 11px;
    letter-spacing: 0.5px;
    text-transform: uppercase;
    line-height: 1.45;
  }
  .mission__line--strong { font-size: 13px; }
  .contact-band {
    position: absolute;
    left: 0;
    right: 0;
    bottom: 38px;
    height: 28px;
    background: var(--band);
    color: var(--band-ink);
    font-size: 8px;
    display: flex;
    align-items: center;
    justify-content: space-between;
    padding: 0 14px;
  }
  .contact-band__list { list-style: none; line-height: 1.35; }
  .contact-band__item { display: flex; align-items: center; gap: 5px; }
  .contact-band__icon { width: 7px; height: 7px; fill: var(--band-ink); }
  .contact-band__web { font-size: 9px; }
</style>
</head>
<body>
<main class="folder-spread">
  <section class="cover cover--front">
    <div class="cover__texture" role="img" aria-label="Fine diagonal charcoal pinstripe texture with soft sheen"></div>
    <div class="brand-lockup">
      <span class="brand-lockup__mark" aria-hidden="true"></span>
      <div class="brand-lockup__name">QUORVALE</div>
      <div class="brand-lockup__tagline">COUNTABLE GROWTH</div>
    </div>
  </section>

  <section class="cover cover--back">
    <div class="cover__texture" role="img" aria-label="Fine diagonal charcoal pinstripe texture with soft sheen"></div>
    <div class="mission">
      <span class="mission__emblem" aria-hidden="true"></span>
      <p class="mission__line">Turning insights into actions</p>
      <p class="mission__line mission__line--strong">&amp; Passion into profit</p>
    </div>
    <footer class="contact-band">
      <ul class="contact-band__list">
        <li class="contact-band__item">
          <svg class="contact-band__icon" viewBox="0 0 10 10" aria-hidden="true"><rect x="2.5" y="0" width="5" height="10" rx="1"/></svg>
          04 1234 5678
        </li>
        <li class="contact-band__item">
          <svg class="contact-band__icon" viewBox="0 0 10 10" aria-hidden="true"><path d="M0 2h10v6H0z M0 2l5 3.5L10 2" stroke="#fff" stroke-width="0.6"/></svg>
          info@quorvale.com.au
        </li>
      </ul>
      <span class="contact-band__web">www.quorvale.com.au</span>
    </footer>
  </section>
</main>
</body>
</html>
```